New Wine Label - Argentinian Malbec 'Brisa Dorada'

I am looking for an exceptional and exciting design for a wine label called 'Brisa Dorada' meaning Golden Breeze or Breeze of Gold. The design must feature the name 'Brisa Dorada', a star logo and the word 'Malbec'. It will also need the words 'Mendoza, Argentina' at the bottom of the label as a prominent piece of information. Please produce the work in size 80mm x 100mm. Feel free to use colour in addition to black/white and ensue that the label is easy to read on a shelf placement.

Target Market(s)

25-50 Year Olds who enjoy great wine that looks and appears interesting and a little different.

Requirements
Must have
• Star Logo
• Word - Malbec
• Words - Mendoza, Argentina
Nice to have
• Background image to label

```html
<!DOCTYPE html>
<html lang="en">
<head>
<meta charset="utf-8">
<title>Brisa Dorada Malbec Label</title>
<link rel="stylesheet" href="https://fonts.googleapis.com/css2?family=Great+Vibes&family=Marck+Script&display=swap">
<style>
  :root {
    --backdrop: #e3e8ee;
    --paper: #ffffff;
    --ink: #050505;
    --gold: #e2c36e;
    --gold-deep: #c9a545;
    --gold-pale: #f1dfa6;
    --pattern-gold: #f6ebc9;
    --pattern-grey: #2a2a2a;
  }
  html, body {
    margin: 0;
    padding: 0;
    width: 1138px;
    height: 1200px;
    overflow: hidden;
    background: var(--backdrop);
  }
  .canvas {
    position: relative;
    width: 1138px;
    height: 1200px;
  }
  .label {
    position: absolute;
    left: 89px;
    top: 149px;
    width: 960px;
    height: 902px;
    background: var(--paper);
    box-shadow: 0 0 0 3px var(--gold);
    overflow: hidden;
  }
  .label-art {
    position: absolute;
    inset: 0;
    width: 100%;
    height: 100%;
  }
  .brand-mark {
    position: absolute;
    left: 34px;
    top: 40px;
    display: flex;
    align-items: center;
    gap: 10px;
    font-family: "Great Vibes", cursive;
    font-size: 30px;
    color: var(--gold-deep);
  }
  .brand-mark .dot {
    width: 34px;
    height: 34px;
    border-radius: 50%;
    background: var(--gold);
  }
  .varietal {
    position: absolute;
    left: 200px;
    top: 80px;
    font-family: "Great Vibes", cursive;
    font-size: 60px;
    color: var(--ink);
    line-height: 1;
  }
  .wine-name {
    position: absolute;
    left: 150px;
    top: 400px;
    width: 620px;
    text-align: center;
    font-family: "Marck Script", cursive;
    font-size: 84px;
    line-height: 1;
    color: var(--gold);
  }
  .origin {
    position: absolute;
    left: 451px;
    top: 818px;
    width: 509px;
    height: 84px;
    display: flex;
    align-items: center;
    justify-content: center;
    font-family: "Great Vibes", cursive;
    font-size: 58px;
    color: var(--ink);
  }
</style>
</head>
<body>
<main class="canvas">
  <section class="label">
    <svg class="label-art" viewBox="0 0 1000 940" preserveAspectRatio="none" aria-hidden="false">
      <defs>
        <linearGradient id="origin-band" x1="0" y1="0" x2="1" y2="0">
          <stop offset="0" stop-color="#e9cf85"/>
          <stop offset="0.5" stop-color="#dcbc62"/>
          <stop offset="1" stop-color="#ecd595"/>
        </linearGradient>
        <radialGradient id="pattern-light" cx="0.5" cy="0.5" r="0.5">
          <stop offset="0" stop-color="#f8eed0"/>
          <stop offset="1" stop-color="#ffffff" stop-opacity="0"/>
        </radialGradient>
        <radialGradient id="pattern-dark" cx="0.5" cy="0.5" r="0.5">
          <stop offset="0" stop-color="#333333"/>
          <stop offset="1" stop-color="#050505" stop-opacity="0"/>
        </radialGradient>
      </defs>

      <g class="pattern-area" role="img" aria-label="Gold lace pattern of rings on the white field">
        <ellipse cx="300" cy="330" rx="260" ry="200" fill="url(#pattern-light)"/>
        <ellipse cx="760" cy="640" rx="250" ry="190" fill="url(#pattern-light)"/>
      </g>

      <path class="ribbon" fill="var(--ink)"
        d="M560 0 L1000 0 L1000 340 C1000 470 960 520 860 520 L550 520 C490 520 470 560 470 620 L470 940 L0 940 L0 620 C0 470 60 405 165 405 L455 405 C525 405 540 370 540 300 L540 40 C540 18 548 0 560 0 Z"/>

      <g class="pattern-area" role="img" aria-label="Grey lace pattern of rings on the black ribbon">
        <ellipse cx="780" cy="200" rx="220" ry="170" fill="url(#pattern-dark)"/>
        <ellipse cx="230" cy="760" rx="230" ry="170" fill="url(#pattern-dark)"/>
      </g>

      <rect class="origin-band" x="470" y="850" width="530" height="90" fill="url(#origin-band)"/>
    </svg>

    <div class="brand-mark"><span class="dot"></span><span>Brisa Dorada</span></div>
    <div class="varietal">Malbec</div>
    <h1 class="wine-name" style="margin:0;font-weight:400;">Brisa Dorada</h1>
    <div class="origin">Mendoza, Argentina</div>
  </section>
</main>
</body>
</html>
```